Accident Law Firm Billboard Bold Easy to See Car Accidents

We need a billboard design that can catch attention in a very crowed Car Accident lawyer market. We wish to feature the phone number (407) 555-0148 as the focus of the Bill Board. We are trying to get the phone number recognized and remembered by drivers. The law firm name is not as crucial to remember.
Basically, It's CAR ACCIDENT? Then (407) 555-0148. We are not married to any specific color scheme but it has to POP and catch attention.
So the Crucial elements are as follows:
1. Phone number (407) 555-0148
2. Words CAR ACCIDENT?
3. Firm Logo in lower portion or where appropriate. Firm Logo to be provided
4. We may want to try a Day Glow orange color, with White and Black added. An example of the color scheme shall be provided.
5. Possible "Catch Phrase" to be used, "It's Time Call 9"
Target Market(s)
Orlando Florida Car Accident victims
Industry/Entity Type
Law Firm
Requirements
Must have
- Easy to see phone number (407) 555-0148
- Catch attention
Nice to have
- I would like to have the sign visible in bright sunlight and it not too hard to immediately know what phone number is for
Should not have
- too many words
- No bold enough
- confusing fonts
- Unclear fonts

```html
<!DOCTYPE html>
<html lang="en">
<head>
<meta charset="utf-8">
<title>Marlowe Law – Accident Billboard</title>
<link rel="stylesheet" href="https://fonts.googleapis.com/css2?family=Montserrat:wght@400;500;700;800&display=swap">
<style>
  :root {
    --backdrop: #e9e9e7;
    --board-orange: #e8874a;
    --board-shade: #d9773c;
    --icon-tint: #f1c3a2;
    --ink-dark: #2a2623;
    --ink-white: #ffffff;
    --number-shadow: #5a4334;
    --frame-line: rgba(255, 255, 255, 0.3);
  }
  * { margin: 0; padding: 0; box-sizing: border-box; }
  html, body {
    width: 1200px;
    height: 800px;
    overflow: hidden;
    background: var(--backdrop);
  }
  .canvas {
    position: relative;
    width: 1200px;
    height: 800px;
  }
  .billboard {
    position: absolute;
    left: 40px;
    top: 190px;
    width: 1120px;
    height: 420px;
    background: var(--board-orange);
    overflow: hidden;
    font-family: "Montserrat", sans-serif;
    color: var(--ink-dark);
  }
  .headline {
    position: absolute;
    left: 52px;
    top: 62px;
    font-size: 40px;
    line-height: 48px;
    font-weight: 400;
    letter-spacing: 0.5px;
  }
  .tagline {
    position: absolute;
    right: 640px;
    top: 128px;
    font-size: 18px;
    line-height: 22px;
    font-weight: 500;
    letter-spacing: 0.5px;
    white-space: nowrap;
  }
  .number-frame {
    position: absolute;
    left: 40px;
    top: 162px;
    width: 490px;
    height: 130px;
    border: 1px solid var(--frame-line);
  }
  .phone-number {
    position: absolute;
    left: 52px;
    top: 190px;
    font-size: 56px;
    line-height: 68px;
    font-weight: 800;
    letter-spacing: -1px;
    white-space: nowrap;
    color: var(--ink-white);
    text-shadow: 3px 4px 0 var(--number-shadow), 5px 7px 6px rgba(0, 0, 0, 0.25);
  }
  .firm-name {
    position: absolute;
    left: 44px;
    top: 300px;
    font-size: 12px;
    line-height: 16px;
    font-weight: 700;
    letter-spacing: 1px;
    text-transform: uppercase;
  }
  .seat-art {
    position: absolute;
    left: 560px;
    top: 0;
    width: 560px;
    height: 420px;
  }
</style>
</head>
<body>
  <main class="canvas">
    <section class="billboard" aria-label="Accident law firm billboard">
      <h1 class="headline">ACCIDENT ?</h1>
      <p class="tagline">ITS TIME TO CALL</p>
      <div class="number-frame"></div>
      <p class="phone-number">(407) 555-0148</p>
      <p class="firm-name">Marlowe Law</p>
      <svg class="seat-art" viewBox="0 0 560 420" role="img" aria-label="Line icon of a car seat with a deployed airbag, casting a long shadow">
        <polygon points="60,120 560,420 260,420 40,300" fill="var(--board-shade)"/>
        <rect x="30" y="80" width="220" height="260" rx="40" fill="var(--icon-tint)" opacity="0.55"/>
      </svg>
    </section>
  </main>
</body>
</html>
```